artist "stamp" design

Im a young artist. I`m making a stamp with my information so i can make homemade business cards, so I need the following information to look good together and simple to read:

Lorena Batalla Quiroga

www.lorebtqz.com

lorenabq47@fotmail.example

i want a very clan look, but with some personality. a simple logo or "look" would be great but nothing to fancy.

An idea I had was to make it look like it was written with a typewriter or a concept like that...be creative! thank you!
Updates

I don't want any image or icon, just letters, I need it to be compacto, I'm making a stamp

I don't want it to say photography 

I dont want my name to take over so it should stay close to the size as the rest of the info.

all my info should be included, this is not a logo its a design for a stamp meant to fin in a business card.

Target Market(s)

I'm a photographer, I want something very simple and I need this to make a stamp that ill use to pit on my cards and CV. I want something simple and modern

Industry/Entity Type

Business

Logo Text

Lorena Batalla Quiroga

Logo styles of interest
Abstract Logo
Wordmark Logo
Lettermark Logo
Font styles to use
Serif
Sans Serif

Requirements
Must have
• Has to look young and fresh
Nice to have
• Have to see how it looks on a business card with website and and email
Should not have
• Images

```html
<!DOCTYPE html>
<html lang="en">
<head>
<meta charset="utf-8">
<title>Lorena Batalla Quiroga — Stamp</title>
<link rel="stylesheet" href="https://fonts.googleapis.com/css2?family=Black+Ops+One&family=Special+Elite&display=swap">
<style>
  :root {
    --paper: #ffffff;
    --ink: #5a5a5a;
    --ink-band: #5e5e5e;
    --ink-reverse: #ffffff;
  }
  html, body {
    margin: 0;
    padding: 0;
    width: 1200px;
    height: 1000px;
    overflow: hidden;
    background: var(--paper);
  }
  .canvas {
    position: relative;
    width: 1200px;
    height: 1000px;
  }
  .stamp {
    position: absolute;
    left: 209px;
    top: 408px;
    width: 781px;
  }
  .stamp__name {
    display: block;
    width: 781px;
    height: 52px;
  }
  .stamp__name text {
    font-family: "Black Ops One", "Arial Black", sans-serif;
    font-size: 57px;
    fill: var(--ink);
  }
  .stamp__email {
    margin-top: 7px;
    height: 65px;
    background: var(--ink-band);
    color: var(--ink-reverse);
    font-family: "Special Elite", "Courier New", monospace;
    font-size: 40px;
    line-height: 65px;
    text-align: center;
    letter-spacing: 0.5px;
  }
  .stamp__web {
    margin-top: 4px;
    color: var(--ink);
    font-family: "Special Elite", "Courier New", monospace;
    font-size: 42px;
    line-height: 50px;
    text-align: center;
    letter-spacing: 1px;
  }
</style>
</head>
<body>
  <main class="canvas">
    <section class="stamp">
      <svg class="stamp__name" viewBox="0 0 781 52" aria-label="Lorena Batalla Quiroga">
        <text x="0" y="47" textLength="781" lengthAdjust="spacingAndGlyphs">LORENA BATALLA QUIROGA</text>
      </svg>
      <div class="stamp__email">lorenabq47@fotmail.example</div>
      <div class="stamp__web">www.lorebtqz.com</div>
    </section>
  </main>
</body>
</html>
```